Booklet - I can pay more Urgent Project

Dear,
I need help to design a booklet for my startup, I have provided a booklet sample I want the same layout and organization. As you can see I'm not looking for a lot of colors or graphs, it should clean neat. The booklet size could be 8.5 x 11 or 8.5x5.5. This is urgent I need it in 24hr max.
My booklet content on word file named "Moss Lantern Booklet".
Booklet sample is on pdf file named "bookt_sample".
Nice cover design is helpful
Thank you.

Requirements
Must have
• Need to go to print by tomorrow - urgent project

```html
<!DOCTYPE html>
<html lang="en">
<head>
<meta charset="utf-8">
<title>Moss Lantern.net — Booklet Cover</title>
<link rel="stylesheet" href="https://fonts.googleapis.com/css2?family=Open+Sans:wght@300;400;600;700&display=swap">
<style>
  :root {
    --frame-gold: #d4a62c;
    --page-white: #ffffff;
    --ink-dark: #58595b;
    --accent-blue: #1f9ad6;
    --band-grey: #8c8c8c;
    --band-text: #ececec;
    --art-light: #f1f1f1;
    --art-mid: #b9b9b9;
    --art-dark: #7c7c7c;
  }
  * { margin: 0; padding: 0; box-sizing: border-box; }
  html, body {
    width: 828px; height: 1200px; overflow: hidden;
    background: var(--frame-gold);
    font-family: "Open Sans", Arial, sans-serif;
  }
  .cover {
    position: relative;
    width: 828px; height: 1200px;
    background: var(--frame-gold);
  }
  .page {
    position: absolute;
    left: 36px; top: 34px;
    width: 758px; height: 1130px;
    background: var(--page-white);
    overflow: hidden;
  }
  .title {
    position: absolute;
    right: 90px; top: 76px;
    font-size: 60px;
    font-weight: 700;
    letter-spacing: -1.5px;
    line-height: 1;
    color: var(--ink-dark);
    white-space: nowrap;
  }
  .title-accent { color: var(--accent-blue); }
  .title-suffix { font-weight: 400; }
  .by-tag {
    position: absolute;
    right: 90px; top: 152px;
    width: 30px; height: 30px;
    background: var(--accent-blue);
    color: var(--page-white);
    font-size: 11px; font-weight: 700;
    display: flex; align-items: center; justify-content: center;
  }
  .authors {
    position: absolute;
    right: 90px; top: 192px;
    font-size: 16px; font-weight: 400;
    letter-spacing: 0.3px;
    color: var(--ink-dark);
    white-space: nowrap;
  }
  .cover-art {
    position: absolute;
    left: 130px; top: 240px;
    width: 500px; height: 600px;
    border-radius: 46% 54% 40% 60% / 50% 44% 56% 50%;
    background:
      radial-gradient(ellipse at 55% 30%, var(--art-dark) 0%, var(--art-mid) 30%, transparent 62%),
      radial-gradient(ellipse at 30% 55%, var(--art-mid) 0%, transparent 55%),
      radial-gradient(ellipse at 50% 50%, var(--art-light) 0%, transparent 72%);
  }
  .footer-band {
    position: absolute;
    left: 0; bottom: 0;
    width: 758px; height: 290px;
  }
  .footer-band svg { display: block; width: 100%; height: 100%; }
  .project-info, .mentors {
    position: absolute;
    top: 976px;
    color: var(--band-text);
    font-weight: 300;
  }
  .project-info { left: 58px; }
  .mentors { right: 70px; text-align: right; }
  .label {
    font-size: 16px;
    margin-bottom: 60px;
  }
  .mentors .label { margin-bottom: 44px; }
  .meta {
    font-size: 11px;
    letter-spacing: 0.5px;
    line-height: 1.55;
  }
  .meta strong { font-weight: 700; }
</style>
</head>
<body>
  <main class="cover">
    <section class="page">
      <h1 class="title">Moss <span class="title-accent">Lantern</span><span class="title-suffix">.net</span></h1>
      <div class="by-tag">BY</div>
      <p class="authors">NADIA FARRELL &amp; OWEN HALVORSEN</p>

      <div class="cover-art" role="img" aria-label="Grey ink-wash illustration of a flowering branch"></div>

      <div class="footer-band">
        <svg viewBox="0 0 758 290" preserveAspectRatio="none" aria-hidden="true">
          <path fill="var(--band-grey)" d="M0 40 C30 22 60 48 95 36 C130 22 150 8 185 24 C215 38 240 30 270 18 C300 6 330 16 360 30 C390 42 420 30 450 22 C490 12 520 18 550 26 C590 36 620 40 650 30 C690 18 720 22 758 12 L758 290 L0 290 Z"/>
        </svg>
      </div>

      <div class="project-info">
        <p class="label">Capstone Project</p>
        <p class="meta">KDT | DEC 30, 2018</p>
      </div>

      <div class="mentors">
        <p class="label">Mentors</p>
        <p class="meta">PROFESSOR <strong>ELLIOT MARSH</strong><br>PROFESSOR <strong>TOMAS VARELA</strong></p>
      </div>
    </section>
  </main>
</body>
</html>
```